Create book cover for a Sudoku puzzle book

It is a sudoku puzzle book for experienced sudoku puzzle solvers. It has over 250 sudoku puzzles ranging from medium level to hard.

Create a book cover closely refer to the reference image. The book cover must look as similar to the reference image as possible, including all the design style, color, illustrations and fonts. Use the sudoku puzzle in the attachment to replace the one on the reference image. All the design elements including fonts must be commercially licensed.

In the final delivery, the cover design must be available in both png/ai and pdf file format. All source files and commercial licenses for the used design elements must also be delivered as well.

Book Title: Grids for Night Owls
Subtitle: 250+ Medium to Hard Puzzles

Book size: 8.5x11 inches
Page count: 171
Paperback Print Book
Platform: Pellora Press

Text on the front cover (all in uppercase):
- Grids for Night Owls
- 250+ Medium to Hard Puzzles
- 2025
- 250+ Puzzles
- large print

Text on spine:
Book title (only title, no subtitle) on the upper part of the spine and author name on the lower part. All in uppercase.

Text on the back cover (on the top):
Thank you for purchasing "Grids for Night Owls." We hope you are enjoying the puzzles and finding them both challenging and fun. If you have a moment, please consider leaving a review on Pellora. Your feedback helps other puzzle enthusiasts discover this book and allows us to continue creating quality content. We appreciate your support and look forward to hearing your thoughts!

Logo on back cover:
-pen name logo, the logo size should be small and subtle. (on bottom middle)

```html
<!DOCTYPE html>
<html lang="en">
<head>
<meta charset="utf-8">
<title>Grids for Night Owls – Cover</title>
<link rel="stylesheet" href="https://fonts.googleapis.com/css2?family=Montserrat:wght@500;600;700;800;900&display=swap">
<style>
  :root {
    --ink: #111214;
    --paper: #ffffff;
    --red: #e2222b;
    --deep-red: #b3121a;
    --yellow: #ffe500;
    --navy: #26324a;
  }
  * { margin: 0; padding: 0; box-sizing: border-box; }
  html, body { width: 1200px; height: 765px; overflow: hidden; background: var(--paper); }
  body { font-family: "Montserrat", Arial, sans-serif; color: var(--ink); }

  .cover { position: relative; width: 1200px; height: 765px; overflow: hidden; background: var(--paper); }

  /* Back cover */
  .back { position: absolute; left: 0; top: 0; width: 567px; height: 765px; }
  .back__ink-top {
    position: absolute; left: 0; top: 0; width: 300px; height: 130px;
    background: radial-gradient(ellipse at 0% 0%, var(--ink) 0 38%, rgba(17,18,20,0.5) 55%, transparent 72%);
  }
  .back__ink-bottom {
    position: absolute; left: 0; bottom: 0; width: 200px; height: 60px;
    background: radial-gradient(ellipse at 0% 100%, var(--ink) 0 30%, rgba(17,18,20,0.4) 55%, transparent 75%);
  }
  .back__message {
    position: absolute; left: 71px; top: 151px; width: 456px;
    font-size: 22.3px; font-weight: 500; line-height: 27.5px; text-align: justify;
  }
  .pen-name {
    position: absolute; left: 249px; top: 582px; width: 98px; height: 98px;
    border-radius: 50%; background: var(--navy); border: 3px solid #b8bcc4;
    display: flex; align-items: center; justify-content: center; text-align: center;
    color: var(--paper); font-size: 10px; font-weight: 700; line-height: 1.2; letter-spacing: 0.3px;
  }

  /* Spine */
  .spine { position: absolute; left: 567px; top: 0; width: 47px; height: 765px; background: var(--paper); }
  .spine__text {
    position: absolute; left: 50%; writing-mode: vertical-rl; transform: translateX(-50%);
    font-weight: 800; font-size: 20px; letter-spacing: 0.5px; white-space: nowrap;
  }
  .spine__title { top: 104px; }
  .spine__author { top: 491px; font-weight: 600; }

  /* Front cover */
  .front { position: absolute; left: 614px; top: 0; width: 586px; height: 765px; background: var(--paper); }
  .front__splash {
    position: absolute; left: 0; top: 200px; width: 586px; height: 505px;
    background:
      radial-gradient(circle at 57% 47%, var(--paper) 0 20%, transparent 34%),
      radial-gradient(ellipse at 57% 47%, var(--red) 0 40%, var(--ink) 58%, var(--deep-red) 68%, rgba(255,255,255,0.2) 88%);
  }
  .large-print {
    position: absolute; left: 104px; top: 0; width: 378px; height: 49px;
    background: var(--yellow); clip-path: polygon(0 0, 100% 0, 92% 100%, 8% 100%);
    display: flex; align-items: center; justify-content: center;
    font-weight: 800; font-size: 24px; letter-spacing: 0.3px;
  }
  .title { position: absolute; left: 0; width: 586px; text-align: center; font-weight: 900; line-height: 1; }
  .title__main { top: 48px; font-size: 104px; letter-spacing: 1px; }
  .title__sub { top: 150px; font-size: 30px; font-weight: 800; }
  .year {
    position: absolute; left: 235px; top: 189px; width: 107px; height: 33px;
    border-radius: 10px; background: var(--red); color: var(--paper);
    display: flex; align-items: center; justify-content: center;
    font-weight: 800; font-size: 26px;
  }
  .badge { position: absolute; left: 433px; top: 212px; width: 124px; height: 124px; }
  .badge__label {
    position: absolute; left: 433px; top: 212px; width: 124px; height: 124px;
    display: flex; flex-direction: column; align-items: center; justify-content: center;
    font-weight: 900; line-height: 1;
  }
  .badge__count { font-size: 33px; }
  .badge__word { font-size: 15px; margin-top: 4px; }
  .puzzle { position: absolute; left: 184px; top: 315px; width: 201px; height: 201px; background: var(--paper); }
  .puzzle text { font-family: "Montserrat", Arial, sans-serif; font-weight: 600; font-size: 19px; fill: var(--ink); }
  .front__band {
    position: absolute; left: 0; top: 704px; width: 586px; height: 61px; background: var(--ink);
    color: var(--paper); display: flex; align-items: center; justify-content: center;
    font-weight: 800; font-size: 30px; letter-spacing: 0.3px;
  }
</style>
</head>
<body>
<div class="cover">

  <section class="back">
    <div class="back__ink-top" role="img" aria-label="Black and red ink brush splatter in the corner"></div>
    <div class="back__ink-bottom" role="img" aria-label="Black ink brush splatter along the bottom edge"></div>
    <p class="back__message">Thank you for purchasing "Grids for Night Owls." We hope you are enjoying the puzzles and finding them both challenging and fun. If you have a moment, please consider leaving a review on Pellora. Your feedback helps other puzzle enthusiasts discover this book and allows us to continue creating quality content. We appreciate your support and look forward to hearing your thoughts!</p>
    <div class="pen-name">THEO<br>VANDAMME</div>
  </section>

  <section class="spine">
    <span class="spine__text spine__title">GRIDS FOR NIGHT OWLS</span>
    <span class="spine__text spine__author">THEO VANDAMME</span>
  </section>

  <section class="front">
    <div class="front__splash" role="img" aria-label="Explosive red, black and white ink paint splash radiating from the centre"></div>
    <div class="large-print">LARGE PRINT</div>
    <h1 class="title title__main">GRIDS</h1>
    <h2 class="title title__sub">FOR NIGHT OWLS</h2>
    <div class="year">2025</div>

    <svg class="badge" viewBox="0 0 124 124" aria-hidden="true">
      <polygon fill="#e2222b" points="62,0 69,10 80,3 84,15 96,11 96,23 109,23 105,35 117,40 109,49 119,57 109,64 118,73 106,78 111,90 98,91 99,104 87,101 84,113 73,107 67,119 59,109 50,118 45,106 33,111 31,98 18,99 21,87 9,82 17,72 6,64 16,57 7,48 18,42 13,31 26,30 24,17 37,19 39,7 50,13"/>
      <circle cx="62" cy="60" r="47" fill="#ffe500"/>
    </svg>
    <div class="badge__label"><span class="badge__count">250+</span><span class="badge__word">PUZZLES</span></div>

    <svg class="puzzle" viewBox="0 0 270 270" role="img" aria-label="Sudoku puzzle grid">
      <g stroke="#111214" stroke-width="0.8">
        <line x1="30" y1="0" x2="30" y2="270"/><line x1="60" y1="0" x2="60" y2="270"/>
        <line x1="120" y1="0" x2="120" y2="270"/><line x1="150" y1="0" x2="150" y2="270"/>
        <line x1="210" y1="0" x2="210" y2="270"/><line x1="240" y1="0" x2="240" y2="270"/>
        <line x1="0" y1="30" x2="270" y2="30"/><line x1="0" y1="60" x2="270" y2="60"/>
        <line x1="0" y1="120" x2="270" y2="120"/><line x1="0" y1="150" x2="270" y2="150"/>
        <line x1="0" y1="210" x2="270" y2="210"/><line x1="0" y1="240" x2="270" y2="240"/>
      </g>
      <g stroke="#111214" stroke-width="3" fill="none">
        <rect x="1.5" y="1.5" width="267" height="267"/>
        <line x1="90" y1="0" x2="90" y2="270"/><line x1="180" y1="0" x2="180" y2="270"/>
        <line x1="0" y1="90" x2="270" y2="90"/><line x1="0" y1="180" x2="270" y2="180"/>
      </g>
      <g text-anchor="middle">
        <text x="45" y="22">2</text><text x="135" y="22">5</text><text x="255" y="22">9</text>
        <text x="15" y="52">4</text><text x="105" y="52">7</text><text x="225" y="52">2</text>
        <text x="75" y="82">9</text><text x="165" y="82">3</text><text x="195" y="82">4</text>
        <text x="15" y="112">2</text><text x="135" y="112">6</text><text x="225" y="112">9</text>
        <text x="75" y="142">4</text><text x="105" y="142">8</text><text x="255" y="142">1</text>
        <text x="45" y="172">9</text><text x="165" y="172">1</text><text x="195" y="172">5</text>
        <text x="75" y="202">2</text><text x="105" y="202">6</text><text x="225" y="202">7</text>
        <text x="15" y="232">6</text><text x="135" y="232">7</text><text x="255" y="232">2</text>
        <text x="45" y="262">7</text><text x="165" y="262">2</text><text x="195" y="262">6</text>
      </g>
    </svg>

    <div class="front__band">250+ MEDIUM TO HARD PUZZLES</div>
  </section>

</div>
</body>
</html>
```